BrightWell is the name of the business, it is a disability service where we offer

Assist-Life Stage, Transition

Household Tasks

Group/Centre Activities

Support Coordination

Innov Community Participation

Home Modification

Participate Community

Assist Personal Activities

Community Nursing Care

Development-Life Skills

Personal Activities High

Assist-Travel/Transport

Assist Access/Maintain Employ

Daily Tasks/Shared Living

Assist Prod-Pers Care/Safety

Assistive Prod-Household Task

Hi, I have uploaded the pictures and short clips. please make them look cohesive and professional I trust you and seen your previous work. many thanks

Target Market(s)

Everyone

Coding

Coded - Design and coding required

Number of Pages Required

2 page

Requirements
Must have
• must be inviting and warm. this is for a disability service that I am passionate about and work from my heart. it must state all the services I offer and contact details. I have attached my Logo
• contact number 0481936027
• once I have a facebook page and a insta and snapchat is then ok to add them because I don't have any social media right now.

```html
<!DOCTYPE html>
<html lang="en">
<head>
<meta charset="utf-8">
<title>BrightWell – Disability Services</title>
<link href="https://fonts.googleapis.com/css2?family=Poppins:wght@300;400;500;600;700&family=Open+Sans:wght@400;600&display=swap" rel="stylesheet">
<style>
:root{
  --green:#1a9e6e;
  --green-dark:#117a55;
  --teal:#2fa98a;
  --lime:#7cc243;
  --ink:#222;
  --body:#555;
  --muted:#888;
  --light:#f3f3f3;
  --dark:#1c1f1e;
  --white:#fff;
}
*{box-sizing:border-box;margin:0;padding:0}
html,body{width:1200px;height:3965px;overflow:hidden}
body{position:relative;font-family:"Open Sans",sans-serif;color:var(--body);background:var(--white)}
.abs{position:absolute}
h1,h2,h3,h4,.nav,.btn{font-family:"Poppins",sans-serif}

/* top bar */
.topbar{left:0;top:0;width:1200px;height:32px;background:var(--green);color:var(--white);font-size:13px}
.topbar .call{left:132px;top:7px;display:flex;align-items:center;gap:8px}
.topbar .search{left:724px;top:6px;width:272px;height:20px;background:var(--white);border-radius:10px;color:#999;font-size:10px;padding:3px 12px;display:flex;justify-content:space-between}
.topbar .lang{left:1018px;top:7px;font-size:12px}

/* header */
.header{left:0;top:32px;width:1200px;height:90px;background:var(--white)}
.brand{display:flex;align-items:center;gap:10px}
.brand .dot{width:42px;height:42px;border-radius:50%;background:var(--green)}
.brand .name{font-family:"Poppins",sans-serif;font-weight:600;font-size:30px;color:var(--green)}
.header .brand{left:132px;top:22px}
.nav{right:134px;top:34px;display:flex;gap:30px;font-size:15px;font-weight:500;color:var(--ink);letter-spacing:.5px}
.nav .active{color:var(--green)}

/* hero */
.hero{left:0;top:122px;width:1200px;height:618px;background:linear-gradient(110deg,#8a9a5b 0%,#c9b99a 30%,#6f8f4e 60%,#3f6b33 100%)}
.hero-title{left:732px;top:272px;font-size:44px;line-height:54px;font-weight:700;color:var(--white)}
.hero-text{left:734px;top:386px;width:310px;font-size:14px;line-height:22px;color:var(--white)}
.btn-appoint{left:734px;top:480px;width:240px;height:44px;border-radius:22px;background:var(--lime);color:var(--white);font-weight:600;font-size:15px;display:flex;align-items:center;justify-content:center;letter-spacing:.5px}
.arrow{width:32px;height:32px;border-radius:50%;background:rgba(0,0,0,.55);display:flex;align-items:center;justify-content:center}
.hero-curve{left:0;top:600px}

/* section headings */
.mark{width:28px;height:28px;border-radius:50%;background:var(--green)}
.sec-title{width:1200px;left:0;text-align:center;font-size:29px;font-weight:700;color:var(--ink);letter-spacing:1px}

/* services */
.card{width:292px;height:235px;box-shadow:0 4px 10px rgba(0,0,0,.18)}
.card .photo{width:100%;height:193px}
.card .label{height:42px;background:var(--teal);color:var(--white);font-family:"Poppins",sans-serif;font-size:17px;display:flex;align-items:center;justify-content:center}
.service-list{left:132px;top:1428px;width:936px;text-align:center;font-size:12px;line-height:20px;color:var(--body)}
.service-list span{color:var(--teal);padding:0 6px}
.btn-more{left:497px;top:1484px;width:206px;height:36px;border:2px solid var(--teal);border-radius:18px;color:var(--teal);font-size:13px;font-weight:600;display:flex;align-items:center;justify-content:center;letter-spacing:1px}

/* welcome */
.welcome{left:0;top:1623px;width:1200px;height:440px;background:linear-gradient(90deg,#128a5c 0%,#1fa06a 50%,#35b06c 100%);clip-path:polygon(0 4%,100% 0,100% 100%,0 96%)}
.welcome-photo{left:98px;top:1592px;width:470px;height:470px;border-radius:50%;border:6px solid var(--white);background:radial-gradient(circle at 50% 40%,#c7b08a,#6a8c4a 70%)}
.welcome-title{left:634px;top:1718px;font-size:29px;font-weight:600;color:var(--white);letter-spacing:.5px}
.welcome-text{left:634px;top:1775px;width:430px;font-size:13px;line-height:27px;color:var(--white)}
.btn-read{left:634px;top:1935px;width:116px;height:36px;border:2px solid var(--white);border-radius:18px;color:var(--white);font-size:13px;font-weight:600;display:flex;align-items:center;justify-content:center}

/* testimonials */
.testi{left:0;top:2062px;width:1200px;height:582px;background:var(--light)}
.testi-label{left:132px;top:2175px;display:flex;align-items:center;gap:10px;font-family:"Poppins",sans-serif;font-size:20px;color:var(--teal);font-weight:500}
.testi-title{left:132px;top:2215px;width:400px;font-size:21px;line-height:30px;font-weight:500;color:#333}
.quote{left:132px;top:2296px;width:380px;font-size:16px;line-height:28px;color:#444}
.quote b{color:var(--teal);font-size:22px}
.author{left:132px;top:2465px;display:flex;align-items:center;gap:14px;font-size:12px;color:#333}
.author .avatar{width:48px;height:48px;border-radius:50%;background:#c19b74}
.dots{left:132px;top:2555px;display:flex;gap:9px}
.dots i{width:7px;height:7px;border-radius:50%;background:#cfcfcf}
.dots i.on{background:var(--teal)}
.video{left:573px;top:2178px;width:495px;height:346px;border-radius:8px;background:linear-gradient(135deg,#a7c46a,#6a9a3c 55%,#4d7a2c);box-shadow:0 3px 8px rgba(0,0,0,.2)}
.play{left:794px;top:2326px;width:54px;height:54px;border-radius:50%;background:rgba(0,0,0,.75);display:flex;align-items:center;justify-content:center}

/* news */
.news{width:280px}
.news .head{display:flex;gap:14px}
.news .date{flex:none;width:32px;height:40px;background:var(--green);color:var(--white);font-size:11px;font-weight:700;text-align:center;line-height:14px;padding-top:5px;font-family:"Poppins",sans-serif}
.news .date span{display:block;background:var(--lime);margin-top:5px;font-weight:400;font-size:10px;line-height:16px}
.news h4{font-size:15px;line-height:22px;font-weight:500;color:var(--ink)}
.news p{margin-top:20px;font-size:11.5px;line-height:22px;color:var(--body)}
.news .more{margin-top:32px;font-size:11px;font-weight:600;color:var(--ink);text-decoration:underline;display:block}

/* contact */
.contact{left:0;top:3185px;width:1200px;height:507px;background:linear-gradient(100deg,#151716,#2a2d2c 60%,#1c1f1e);clip-path:polygon(0 0,100% 20%,100% 100%,0 100%)}
.contact-title{left:132px;top:3320px;font-size:27px;font-weight:600;color:var(--white)}
.contact-rule{left:132px;top:3372px;width:100px;height:2px;background:var(--white)}
.contact-text{left:132px;top:3397px;width:520px;font-size:13px;line-height:22px;color:#ddd}
.info{left:132px;display:flex;align-items:center;gap:22px;color:var(--white);font-size:14px;line-height:20px}
.info .ic{width:36px;height:36px;border:2px solid var(--white);border-radius:50%;display:flex;align-items:center;justify-content:center}
.form{left:714px;top:3161px;width:354px;height:471px;background:var(--white);box-shadow:0 4px 14px rgba(0,0,0,.2);padding:28px 26px}
.form h3{font-size:21px;font-weight:700;color:var(--ink);text-align:center;margin-bottom:18px}
.field{height:36px;border:1px solid #ddd;font-size:11px;color:#777;padding:10px;margin-bottom:12px}
.field.tall{height:60px}
.btn-send{height:38px;background:var(--teal);color:var(--white);font-family:"Poppins",sans-serif;font-weight:600;font-size:14px;display:flex;align-items:center;justify-content:center;margin-top:20px}

/* footer */
.footer .brand{left:0;width:1200px;top:3735px;justify-content:center}
.foot-links{left:0;width:1200px;top:3812px;text-align:center;font-size:13px;color:#333}
.copy{left:0;width:1200px;top:3847px;text-align:center;font-size:13px;color:#333}
.social{left:0;width:1200px;top:3890px;display:flex;justify-content:center;gap:12px}
.social i{width:22px;height:22px;border-radius:3px;background:var(--green)}
</style>
</head>
<body>

<div class="abs topbar">
  <div class="abs call">
    <svg width="12" height="12" viewBox="0 0 24 24"><path fill="#fff" d="M6.6 10.8a15 15 0 006.6 6.6l2.2-2.2c.3-.3.7-.4 1-.2 1.1.4 2.3.6 3.6.6.6 0 1 .4 1 1V20c0 .6-.4 1-1 1A17 17 0 013 4c0-.6.4-1 1-1h3.5c.6 0 1 .4 1 1 0 1.3.2 2.5.6 3.6.1.3 0 .7-.2 1z"/></svg>
    <span>Call Us : 0481 936 027</span>
  </div>
  <div class="abs search"><span>Search item</span><span>&#9906;</span></div>
  <div class="abs lang">EN &nbsp;|&nbsp; FR</div>
</div>

<header class="abs header">
  <div class="abs brand"><span class="dot"></span><span class="name">BrightWell</span></div>
  <nav class="abs nav"><span class="active">HOME</span><span>ABOUT US</span><span>OUR SERVICES</span><span>BLOG</span><span>CONTACT US</span></nav>
</header>

<section class="abs hero" role="img" aria-label="Carer smiling with an elderly woman in a wheelchair in a leafy park"></section>
<h1 class="abs hero-title">COMMUNITY<br>NURSING CARE</h1>
<p class="abs hero-text">Lorem ipsum dolor sit amet, consectetur adipiscing elit, sed do eiusmod tempor incididunt ut labore et dolore</p>
<div class="abs btn btn-appoint">MAKE AN APPOINTMENT</div>
<div class="abs arrow" style="left:66px;top:382px"><svg width="12" height="12" viewBox="0 0 12 12"><path d="M8 1L3 6l5 5" stroke="#fff" stroke-width="2" fill="none"/></svg></div>
<div class="abs arrow" style="left:1098px;top:382px"><svg width="12" height="12" viewBox="0 0 12 12"><path d="M4 1l5 5-5 5" stroke="#fff" stroke-width="2" fill="none"/></svg></div>
<svg class="abs hero-curve" width="1200" height="150" viewBox="0 0 1200 150">
  <path d="M0 120 Q300 40 600 110 T1200 20 V150 H0Z" fill="#fff"/>
  <path d="M0 120 Q300 40 600 110 T1200 20" stroke="#1a9e6e" stroke-width="8" fill="none"/>
  <path d="M100 110 Q350 50 650 90" stroke="#7cc243" stroke-width="6" fill="none" stroke-linecap="round"/>
</svg>

<div class="abs mark" style="left:586px;top:792px"></div>
<h2 class="abs sec-title" style="top:826px">OUR SERVICES</h2>

<div class="abs card" style="left:132px;top:912px"><div class="photo" role="img" aria-label="Older woman smiling at home while doing household tasks" style="background:linear-gradient(135deg,#c9a98a,#8d7560)"></div><div class="label">Household Tasks</div></div>
<div class="abs card" style="left:455px;top:912px"><div class="photo" role="img" aria-label="Man reading in a wheelchair in a modified home" style="background:linear-gradient(135deg,#d8cdbb,#9a8a74)"></div><div class="label">Home Modification</div></div>
<div class="abs card" style="left:774px;top:912px"><div class="photo" role="img" aria-label="Man in a wheelchair raising his arms outdoors among trees" style="background:linear-gradient(135deg,#9cb56a,#5d7d3a)"></div><div class="label">Development-Life Skills</div></div>
<div class="abs card" style="left:132px;top:1181px"><div class="photo" role="img" aria-label="Carer pushing a smiling man in a wheelchair outside" style="background:linear-gradient(135deg,#b89a78,#6e5b48)"></div><div class="label">Community Nursing Care</div></div>
<div class="abs card" style="left:455px;top:1181px"><div class="photo" role="img" aria-label="Young man in a sports wheelchair holding a ball" style="background:linear-gradient(135deg,#7fa0a8,#4a6670)"></div><div class="label">Personal Activities High</div></div>
<div class="abs card" style="left:774px;top:1181px"><div class="photo" role="img" aria-label="Group of people raising hands together in a park" style="background:linear-gradient(135deg,#a8c070,#5f8a3e)"></div><div class="label">Participate Community</div></div>

<p class="abs service-list">Assist-Life Stage, Transition<span>•</span>Group/Centre Activities<span>•</span>Support Coordination<span>•</span>Innov Community Participation<span>•</span>Assist Personal Activities<br>Assist-Travel/Transport<span>•</span>Assist Access/Maintain Employ<span>•</span>Daily Tasks/Shared Living<span>•</span>Assist Prod-Pers Care/Safety<span>•</span>Assistive Prod-Household Task</p>

<div class="abs btn btn-more">VIEW MORE SERVICES</div>

<section class="abs welcome"></section>
<div class="abs welcome-photo" role="img" aria-label="Two women laughing outdoors with a dog"></div>
<h2 class="abs welcome-title">WELCOME TO BRIGHTWELL</h2>
<p class="abs welcome-text">Sed ut perspiciatis unde omnis iste natus error sit voluptatem accusantium doloremque laudantium, totam rem aperiam, eaque ipsa quae ab illo inventore veritatis et quasi architecto beatae vitae dicta sunt explicabo. Nemo enim ipsam voluptatem quia voluptas sit aspernatur aut odit aut fugit, sed quia consequuntur</p>
<div class="abs btn btn-read">READ MORE</div>

<section class="abs testi"></section>
<div class="abs testi-label"><svg width="22" height="8"><rect width="22" height="2" fill="#2fa98a"/><rect y="6" width="14" height="2" fill="#2fa98a"/></svg>TESTIMONIALS</div>
<h3 class="abs testi-title">Nemo enim ipsam voluptatem<br>quia tas voluptatem</h3>
<p class="abs quote"><b>&laquo;</b> Sed ut perspiciatis unde omnis iste natus error sit voluptatem accusantium doloremque laudantium, totam rem aperiam, eaque ipsa quae ab illo inventore veritatis et quasi architecto beatae vitae dicta <b>&raquo;</b></p>
<div class="abs author"><span class="avatar"></span><span><b style="font-weight:600">JORDAN ELLIS</b><br>BrightWell</span></div>
<div class="abs dots"><i></i><i class="on"></i><i></i><i></i></div>
<div class="abs video" role="img" aria-label="Video still of two women hugging and laughing on the grass"></div>
<div class="abs play"><svg width="18" height="20" viewBox="0 0 18 20"><path d="M2 1l15 9-15 9z" fill="#fff"/></svg></div>

<div class="abs mark" style="left:586px;top:2730px"></div>
<h2 class="abs sec-title" style="top:2770px">LATEST NEWS</h2>

<article class="abs news" style="left:132px;top:2875px">
  <div class="head"><div class="date">03<span>Sep</span></div><h4>QUIS AUTEM VEL EUM IURE REPREHENDERIT</h4></div>
  <p>Sed ut perspiciatis unde omnis iste natus error sit voluptatem accusantium doloremque laudantium, totam rem aperiam, eaque ipsa quae ab illo inventore veritatis et quasi architecto</p>
  <span class="more">READ MORE</span>
</article>
<article class="abs news" style="left:465px;top:2875px">
  <div class="head"><div class="date">03<span>Sep</span></div><h4>QUIS AUTEM VEL EUM IURE REPREHENDERIT</h4></div>
  <p>Sed ut perspiciatis unde omnis iste natus error sit voluptatem accusantium doloremque laudantium, totam rem aperiam, eaque ipsa quae ab illo inventore veritatis et quasi architecto</p>
  <span class="more">READ MORE</span>
</article>
<article class="abs news" style="left:796px;top:2875px">
  <div class="head"><div class="date">03<span>Sep</span></div><h4>QUIS AUTEM VEL EUM IURE REPREHENDERIT</h4></div>
  <p>Sed ut perspiciatis unde omnis iste natus error sit voluptatem accusantium doloremque laudantium, totam rem aperiam, eaque ipsa quae ab illo inventore veritatis et quasi architecto</p>
  <span class="more">READ MORE</span>
</article>

<section class="abs contact"></section>
<h2 class="abs contact-title">CONTACT US</h2>
<div class="abs contact-rule"></div>
<p class="abs contact-text">Sed ut perspiciatis unde omnis iste natus error sit voluptatem accusantium doloremque laudantium, totam rem aperiam, eaque ipsa</p>
<div class="abs info" style="top:3464px"><span class="ic"><svg width="14" height="18" viewBox="0 0 14 18"><path d="M7 0a7 7 0 00-7 7c0 5 7 11 7 11s7-6 7-11a7 7 0 00-7-7zm0 10a3 3 0 110-6 3 3 0 010 6z" fill="#fff"/></svg></span><span>14 Wattle Lane, Greenvale,<br>VIC 3059</span></div>
<div class="abs info" style="top:3525px"><span class="ic"><svg width="14" height="14" viewBox="0 0 24 24"><path fill="#fff" d="M6.6 10.8a15 15 0 006.6 6.6l2.2-2.2c.3-.3.7-.4 1-.2 1.1.4 2.3.6 3.6.6.6 0 1 .4 1 1V20c0 .6-.4 1-1 1A17 17 0 013 4c0-.6.4-1 1-1h3.5c.6 0 1 .4 1 1 0 1.3.2 2.5.6 3.6.1.3 0 .7-.2 1z"/></svg></span><span>Call Us :<br>0481 936 027</span></div>
<div class="abs info" style="top:3586px"><span class="ic"><svg width="16" height="12" viewBox="0 0 16 12"><rect x="1" y="1" width="14" height="10" fill="none" stroke="#fff" stroke-width="1.5"/><path d="M1 1l7 6 7-6" fill="none" stroke="#fff" stroke-width="1.5"/></svg></span><span>E - Mail :<br>info@brightwell.com.au</span></div>

<form class="abs form">
  <h3>SAY HELLO TO BRIGHTWELL</h3>
  <div class="field">Your name *</div>
  <div class="field">Location address *</div>
  <div class="field">Your postcode *</div>
  <div class="field">Phone number *</div>
  <div class="field">Email address *</div>
  <div class="field tall">Your message *</div>
  <div class="btn-send">SEND</div>
</form>

<footer class="footer">
  <div class="abs brand"><span class="dot"></span><span class="name">BrightWell</span></div>
  <div class="abs foot-links">Home &nbsp;|&nbsp; About Us &nbsp;|&nbsp; Our Services &nbsp;|&nbsp; How It Works &nbsp;|&nbsp; Blog &nbsp;|&nbsp; Contact Us</div>
  <div class="abs copy">© 2018 BrightWell. All rights reserved. Privacy Policy &nbsp;|&nbsp; Terms &amp; Conditions</div>
  <div class="abs social"><i></i><i></i><i></i></div>
</footer>

</body>
</html>
```